spot uv business card design for KLT Mechanics

I need a great new business card design best suited for spot uv printing. Details to include are Oliver Haskett 0491227304 wwwkltmech.com.au, oli@kltmech.com.au. Company logo attached.
The design has to be spot uv/varnish optimised!!

```html
<!DOCTYPE html>
<html lang="en">
<head>
<meta charset="utf-8">
<title>KLT Mechanics – Business Card</title>
<link rel="stylesheet" href="https://fonts.googleapis.com/css2?family=Ubuntu:wght@400;500&display=swap">
<style>
  :root {
    --paper: #ffffff;
    --card-white: #ffffff;
    --brand-blue: #3d5a7e;
    --brand-blue-deep: #36506f;
    --uv-tone: #3a5679;
    --edge: #7a7a7a;
    --ink-light: #ffffff;
  }
  * { margin: 0; padding: 0; box-sizing: border-box; }
  html, body {
    width: 1200px;
    height: 711px;
    overflow: hidden;
    background: var(--paper);
    font-family: "Ubuntu", sans-serif;
  }
  .sheet {
    position: relative;
    width: 1200px;
    height: 711px;
  }
  .card {
    position: absolute;
    width: 566px;
    height: 316px;
    border: 1.5px solid var(--edge);
    overflow: hidden;
  }
  .card--front { border-radius: 0 66px 0 66px; }
  .card--back  { border-radius: 66px 0 66px 0; }
  .card--top    { top: 1px; }
  .card--bottom { top: 396px; }
  .card--left   { left: 1px; }
  .card--right  { left: 633px; }

  .card--white { background: var(--card-white); }
  .card--blue  { background: var(--brand-blue); }

  .brand {
    position: absolute;
    left: 78px;
    top: 128px;
    display: flex;
    align-items: center;
    gap: 14px;
  }
  .brand__mark {
    width: 40px;
    height: 40px;
    background: var(--brand-blue);
  }
  .brand__name {
    font-size: 44px;
    font-weight: 400;
    letter-spacing: 0.5px;
    text-transform: uppercase;
    color: var(--brand-blue);
    line-height: 1;
  }
  .brand--varnish .brand__mark { background: var(--brand-blue-deep); }
  .brand--varnish .brand__name { color: var(--brand-blue-deep); }

  .varnish-field {
    position: absolute;
    inset: 0;
    background: linear-gradient(160deg, var(--uv-tone) 0%, var(--brand-blue) 55%, var(--uv-tone) 100%);
  }

  .contact {
    position: absolute;
    left: 0;
    right: 0;
    text-align: center;
    color: var(--ink-light);
  }
  .contact__name {
    top: 118px;
    font-size: 22px;
    font-weight: 500;
  }
  .contact__phone {
    top: 148px;
    font-size: 19px;
    font-weight: 400;
    letter-spacing: 0.5px;
  }
  .contact__web {
    top: 260px;
    font-size: 16px;
    font-weight: 400;
    letter-spacing: 0.3px;
  }
  .contact__divider { margin: 0 6px; }
</style>
</head>
<body>
  <main class="sheet">
    <!-- Front, print version -->
    <section class="card card--front card--white card--top card--left">
      <div class="brand">
        <span class="brand__mark"></span>
        <span class="brand__name">KLT Mechanics</span>
      </div>
    </section>

    <!-- Back, print version -->
    <section class="card card--back card--blue card--top card--right">
      <div class="varnish-field" role="img" aria-label="Tone-on-tone repeating varnish pattern across the card"></div>
      <p class="contact contact__name">Oliver Haskett</p>
      <p class="contact contact__phone">0491 227 304</p>
      <p class="contact contact__web">oli@kltmech.com.au<span class="contact__divider">|</span>www.kltmech.com.au</p>
    </section>

    <!-- Front, spot UV layer -->
    <section class="card card--front card--blue card--bottom card--left">
      <div class="brand brand--varnish">
        <span class="brand__mark"></span>
        <span class="brand__name">KLT Mechanics</span>
      </div>
    </section>

    <!-- Back, spot UV layer -->
    <section class="card card--back card--blue card--bottom card--right">
      <div class="varnish-field" role="img" aria-label="Tone-on-tone repeating varnish pattern across the card"></div>
      <p class="contact contact__name">Oliver Haskett</p>
      <p class="contact contact__phone">0491 227 304</p>
      <p class="contact contact__web">oli@kltmech.com.au<span class="contact__divider">|</span>www.kltmech.com.au</p>
    </section>
  </main>
</body>
</html>
```